Door Hanger for 20% off on dry cleaning

I need a door hanger (3.5" x 8.5" with a hole for the door handle) for a 20% off sale on dry cleaning. The business is called "Suds on Willow" and is a full-service laundry. The store is a laundromat that is used by self-serve customers. We also do wash-and-fold laundry and dry cleaning.

Some requirements:
* Include the logo
* Includes the address of the business:
215 South 700 West
Provo, Utah
(behind Golden Crust Pizza)
* Include some indication of our other services (wash-and-fold laundry, coin laundry, comforters cleaned)
* Offer needs to include an expiration date (say, September 30, 2014).

The door hanger should be full-color with designs for both sides.
Updates

The sale is for 20% off of Dry Cleaning - not the other services. And I'd like both sides of the hanger to mention the sale - in case it gets hung backwards on the door.

Industry/Entity Type

Dry Cleaning

```html
<!DOCTYPE html>
<html lang="en">
<head>
<meta charset="utf-8">
<title>Suds on Willow – Door Hanger</title>
<link href="https://fonts.googleapis.com/css2?family=Arimo:wght@400;700&display=swap" rel="stylesheet">
<style>
  :root {
    --page: #2b1f14;
    --ink-blue: #0f4c7a;
    --deep-blue: #0b5fb8;
    --sky: #2f8de6;
    --pale: #eaf5fc;
    --lilac: #8c8fe0;
    --orange: #f07a1f;
    --white: #ffffff;
    --dash: #2a5d8f;
  }
  * { box-sizing: border-box; margin: 0; padding: 0; }
  html, body {
    width: 1200px; height: 1000px; overflow: hidden;
    background: var(--page);
    font-family: "Arimo", Arial, sans-serif;
  }
  .canvas { position: relative; width: 1200px; height: 1000px; }

  .hanger {
    position: absolute; top: 110px;
    width: 320px; height: 770px;
    overflow: hidden;
    box-shadow: 0 18px 40px rgba(0,0,0,.55);
  }
  .hanger--lilac { left: 245px; }
  .hanger--blue  { left: 635px; }

  .hanger__backdrop { position: absolute; inset: 0; }
  .hanger--lilac .hanger__backdrop {
    background: linear-gradient(180deg, var(--lilac) 0%, #9fc6ef 22%, var(--pale) 45%, var(--white) 65%, var(--pale) 85%, #a9b8ea 100%);
  }
  .hanger--blue .hanger__backdrop {
    background: linear-gradient(180deg, var(--deep-blue) 0%, var(--sky) 20%, #bfe0f7 40%, var(--pale) 60%, var(--white) 70%);
  }
  .hanger__band { position: absolute; left: 0; bottom: 0; width: 320px; height: 270px; }

  .hanger__hole {
    position: absolute; left: 110px; top: 40px;
    width: 100px; height: 100px; border-radius: 50%;
    background: var(--page);
  }

  .brand {
    position: absolute; left: 30px; top: 172px; width: 260px;
    display: flex; align-items: center; gap: 12px;
  }
  .brand__mark { width: 26px; height: 26px; background: var(--deep-blue); flex: none; }
  .brand__name { font-weight: 700; font-size: 32px; color: var(--deep-blue); white-space: nowrap; }

  .services {
    position: absolute; left: 38px; top: 275px; list-style: none;
    color: var(--ink-blue); font-weight: 700; font-size: 20px; line-height: 30px;
  }
  .services li::before {
    content: ""; display: inline-block; width: 7px; height: 7px; border-radius: 50%;
    background: var(--orange); margin-right: 10px; vertical-align: middle;
  }

  .address {
    position: absolute; left: 0; right: 0; top: 392px; text-align: center;
    color: var(--ink-blue); font-weight: 700; font-size: 25px; line-height: 31px;
    text-shadow: 0 0 3px var(--white), 0 0 3px var(--white);
  }
  .address__note { display: block; margin-top: 6px; font-size: 11px; line-height: 14px; color: var(--orange); }

  .coupon {
    position: absolute; left: 22px; right: 22px; top: 540px; height: 190px;
    background: var(--white); border: 2px dashed var(--dash);
    text-align: center; color: var(--ink-blue);
  }
  .coupon__offer { display: flex; justify-content: center; align-items: flex-end; margin-top: 10px; color: var(--orange); font-weight: 700; }
  .coupon__amount { font-size: 98px; line-height: 90px; letter-spacing: -3px; }
  .coupon__unit { display: flex; flex-direction: column; align-items: center; margin-left: 4px; }
  .coupon__pct { font-size: 50px; line-height: 46px; }
  .coupon__off { font-size: 36px; line-height: 34px; }
  .coupon__service { font-weight: 700; font-size: 31px; line-height: 36px; margin-top: 4px; }
  .coupon__expiry { font-weight: 700; font-size: 19px; line-height: 22px; }
</style>
</head>
<body>
<main class="canvas">

  <article class="hanger hanger--lilac">
    <div class="hanger__backdrop" role="img" aria-label="Soft lilac and blue soap bubbles backdrop"></div>
    <div class="hanger__hole"></div>
    <div class="brand"><span class="brand__mark"></span><span class="brand__name">Suds on Willow</span></div>
    <ul class="services">
      <li>wash-and-fold laundry</li>
      <li>coin laundry</li>
      <li>comforters cleaned</li>
    </ul>
    <p class="address">215 South 700 West<br>Provo, Utah
      <span class="address__note">(behind Golden Crust Pizza)</span></p>
    <section class="coupon">
      <div class="coupon__offer"><span class="coupon__amount">20</span>
        <span class="coupon__unit"><span class="coupon__pct">%</span><span class="coupon__off">off</span></span></div>
      <p class="coupon__service">Dry Cleaning</p>
      <p class="coupon__expiry">September 30, 2014</p>
    </section>
  </article>

  <article class="hanger hanger--blue">
    <div class="hanger__backdrop" role="img" aria-label="Bright blue soap bubbles backdrop"></div>
    <svg class="hanger__band" viewBox="0 0 320 270" aria-hidden="true">
      <path d="M0 40 Q160 -10 320 20 L320 270 L0 270 Z" fill="#a9c9f3"/>
      <path d="M0 52 Q160 4 320 32 L320 270 L0 270 Z" fill="#1f7fe0"/>
    </svg>
    <div class="hanger__hole"></div>
    <div class="brand"><span class="brand__mark"></span><span class="brand__name">Suds on Willow</span></div>
    <ul class="services">
      <li>wash-and-fold laundry</li>
      <li>coin laundry</li>
      <li>comforters cleaned</li>
    </ul>
    <p class="address">215 South 700 West<br>Provo, Utah
      <span class="address__note">(behind Golden Crust Pizza)</span></p>
    <section class="coupon">
      <div class="coupon__offer"><span class="coupon__amount">20</span>
        <span class="coupon__unit"><span class="coupon__pct">%</span><span class="coupon__off">off</span></span></div>
      <p class="coupon__service">Dry Cleaning</p>
      <p class="coupon__expiry">September 30, 2014</p>
    </section>
  </article>

</main>
</body>
</html>
```